Valdora necesita diseños de papeleria como tarjeta de presentacion, hoja membretada, sobres...

La papelería corporativa es para una tienda de moda multimarcas ubicada en Ecuador.
Los diseños tienen que ser de acuerdo a los diseños que adjunto.

```html
<!DOCTYPE html>
<html lang="es">
<head>
<meta charset="utf-8">
<title>Valdora — Tarjeta de presentación</title>
<link rel="stylesheet" href="https://fonts.googleapis.com/css2?family=Montserrat:wght@400;500;700&display=swap">
<style>
  :root {
    --backdrop: #1c1c1c;
    --card-dark: #3d3d3f;
    --card-light: #ffffff;
    --ink: #3a3a3c;
    --ink-soft: #2b2b2b;
    --accent: #e8291f;
    --on-dark: #ffffff;
  }
  * { margin: 0; padding: 0; box-sizing: border-box; }
  html, body {
    width: 1200px; height: 878px; overflow: hidden;
    background: var(--backdrop);
    font-family: "Montserrat", sans-serif;
  }
  .stage {
    position: relative; width: 1200px; height: 878px;
  }
  .card {
    position: absolute; left: 310px; width: 580px; height: 331px;
    box-shadow: 0 10px 30px rgba(0,0,0,.55);
  }
  .card--front { top: 56px; background: var(--card-dark); }
  .card--back { top: 468px; background: var(--card-light); }

  .wordmark {
    font-weight: 700; letter-spacing: .28em; text-transform: uppercase;
    display: flex; align-items: center; gap: 14px;
  }
  .wordmark__square {
    width: 12px; height: 12px; background: var(--accent);
  }
  .card--front .wordmark {
    position: absolute; inset: 0; justify-content: center;
    color: var(--on-dark); font-size: 44px;
  }
  .card--back .wordmark {
    position: absolute; top: 52px; left: 0; right: 0; justify-content: center;
    color: var(--ink); font-size: 38px;
  }

  .details {
    position: absolute; top: 180px; left: 0; right: 0;
    display: flex; justify-content: center;
  }
  .person {
    text-align: right; padding-right: 24px;
    border-right: 1.5px solid var(--accent);
    color: var(--ink-soft); font-size: 14px; line-height: 1.5;
    letter-spacing: .04em;
  }
  .person__name {
    color: var(--accent); font-weight: 700; font-size: 21px;
    letter-spacing: .08em; text-transform: uppercase; line-height: 1.2;
  }
  .contact {
    list-style: none; padding-left: 24px;
    color: var(--ink-soft); font-size: 14.5px; line-height: 1.62;
    letter-spacing: .04em;
  }
  .contact li { display: flex; align-items: center; gap: 9px; }
  .contact svg { width: 11px; height: 11px; flex: none; }
  .contact__brand { color: var(--accent); font-weight: 500; }
</style>
</head>
<body>
<main class="stage">
  <section class="card card--front">
    <div class="wordmark">Valdora<span class="wordmark__square"></span></div>
  </section>

  <section class="card card--back">
    <div class="wordmark">Valdora<span class="wordmark__square"></span></div>

    <div class="details">
      <div class="person">
        <p class="person__name">Andrés Molina</p>
        <p class="person__role">Gerente General</p>
        <p class="person__address">Av. Las Palmas y Sucre.<br>Machala, Ecuador</p>
      </div>
      <ul class="contact">
        <li>
          <svg viewBox="0 0 12 12" aria-hidden="true"><path d="M3 1 L5 3.5 L4 5 Q5 7 7 8 L8.5 7 L11 9 L9.5 11 Q4 10.5 1 3 Z" fill="none" stroke="#e8291f" stroke-width="1.2"/></svg>
          +593 7 210-4488
        </li>
        <li>
          <svg viewBox="0 0 12 12" aria-hidden="true"><rect x="3" y="1" width="6" height="10" rx="1" fill="none" stroke="#e8291f" stroke-width="1.2"/><line x1="5" y1="9" x2="7" y2="9" stroke="#e8291f"/></svg>
          +593 99 514-3720
        </li>
        <li>
          <svg viewBox="0 0 12 12" aria-hidden="true"><rect x="1" y="2.5" width="10" height="7" fill="none" stroke="#e8291f" stroke-width="1.2"/><path d="M1 2.5 L6 6.5 L11 2.5" fill="none" stroke="#e8291f" stroke-width="1.2"/></svg>
          info@valdora.com
        </li>
        <li>
          <svg viewBox="0 0 12 12" aria-hidden="true"><circle cx="6" cy="6" r="5" fill="none" stroke="#e8291f" stroke-width="1.1"/><ellipse cx="6" cy="6" rx="2.2" ry="5" fill="none" stroke="#e8291f" stroke-width="1"/><line x1="1" y1="6" x2="11" y2="6" stroke="#e8291f"/></svg>
          <span>www.<span class="contact__brand">valdora</span>.com</span>
        </li>
      </ul>
    </div>
  </section>
</main>
</body>
</html>
```